Technology Company Web Design Project

We are working with BrimCore. They are a technology company and in need of a new website design.
BrimCore helps companies control who (or what) can access which information inside their systems — and under what conditions. Think of them as the traffic controller for digital access and data permissions.
Instead of letting every app, employee, or AI bot freely connect to everything, GatewardIQ makes sure:
• Each one only gets access to what it actually needs.
• That access follows company rules automatically.
• Those rules are enforced the same way everywhere — across apps, servers, and even AI tools.
Some competitor sites to use for inspiration:
https://www.trovanexus.example/en/lp/ac/trovaspire.html
https://www.clearrulekeeper.example
https://www.vondix.example
Thank you for taking the time to consider designing a website for us. We are web developers based in Stockton and Los Angeles, CA, USA. Most of our projects go through the same process. Understanding this process may help you win a project with us. We custom-code all of our websites in-house. We don’t have any requirements as to what tools you use for your design, but we prefer Drafton files. For any design that we label as four-stars, we send it to the client for review. The client picks the final design they want us to use. Once we complete this process, we will continue to show additional clients all the four-star sites and purchase them later. Your designs will have multiple chances to sell. For better chances of success, we ask that you follow these guidelines.
IMAGES:
If you use any images or icons in the design, we ask that you have a link to the asset so we can purchase the image/icon. Most of the designs we submit do not have the customer’s images on them unless they have some great images. Be creative; show us the feeling you are trying to portray with your image choices. Use any royalty-free site you choose. We subscribe to Kelvaro and mainly use their images, but we can purchase images outside of Kelvaro.
PLEASE NOTE: we will not submit designs to clients with watermarks on the images.
FONTS:
We ask that you identify the fonts used in the design. This can be done in a message if you want. We typically use Quillny Fonts and Kelvaro Fonts.
CONTENT:
We're always open to different content and ideas. We often submit designs with stock images so the client can see our vision. We typically take pictures after the website launch to use their images with our vision. Lorem Ipsum is fine for paragraphs, but we ask that you write the headers in correct English. We want to be able to show the vision and identify the sections of the website.
INSPIRATION:
We typically add a couple of links in the brief of websites we like to help you get started in your design.
REVISIONS:
We do not often ask for revisions of the designs unless we see something in the design that may not appeal to the client. If there are slight changes that we want to make, we do that in the development process.
FEEDBACK:
We rarely give feedback on designs during the design process. We are working on many website projects and do not have the time to provide feedback. We usually respond if your request is well thought out and asks specific questions, but a note asking “feedback, please” usually goes unanswered.

```html
<!DOCTYPE html>
<html lang="en">
<head>
<meta charset="UTF-8">
<title>BrimCore — The Traffic Controller for Your Digital Access</title>
<link href="https://fonts.googleapis.com/css2?family=Poppins:wght@400;500;600;700&display=swap" rel="stylesheet">
<style>
:root{
  --navy:#1f3b61;
  --navy-deep:#182f4f;
  --orange:#e8802f;
  --orange-soft:#f2a25f;
  --ink:#111111;
  --muted:#555b66;
  --light:#f5f6f8;
  --white:#ffffff;
  --line:#d7dbe2;
}
*{box-sizing:border-box;margin:0;padding:0}
html,body{width:1200px;height:4101px;overflow:hidden}
body{position:relative;font-family:'Poppins',sans-serif;background:var(--white);color:var(--ink)}
.abs{position:absolute}
.bg-shape{position:absolute;left:0;top:0;width:1200px;height:4101px}
.logo{font-family:'Poppins',sans-serif;font-weight:700;color:var(--navy);letter-spacing:1px;display:flex;align-items:center;gap:8px}
.logo .dot{width:14px;height:14px;border-radius:50%;background:var(--orange)}
.btn{position:absolute;display:flex;align-items:center;justify-content:center;border-radius:30px;font-weight:600;font-size:14px;text-transform:uppercase;color:var(--white);background:var(--orange)}
.btn.ghost{background:transparent;border:1.5px solid var(--white)}
.ph{position:absolute;border-radius:14px}

/* nav */
.nav{left:60px;top:8px;width:1080px;height:88px;background:var(--white);border-radius:44px}
.nav .logo{position:absolute;left:60px;top:30px;font-size:22px}
.nav-links{position:absolute;top:32px;left:0;width:100%;font-size:14px;color:var(--ink)}
.nav-links span{position:absolute;transform:translateX(-50%);white-space:nowrap}
.nav-links .active{color:var(--orange)}
.nav-links .active::after{content:"";position:absolute;left:50%;top:26px;width:6px;height:6px;margin-left:-3px;border-radius:50%;background:var(--orange)}

/* hero */
.hero-title{left:60px;top:188px;font-size:47px;font-weight:600;line-height:56px;color:var(--white)}
.hero-title em{font-style:normal;color:var(--orange)}
.hero-text{left:60px;top:376px;width:520px;font-size:15.5px;line-height:24px;color:var(--white)}

/* headings */
.sec-title{position:absolute;left:0;width:1200px;text-align:center;font-size:35px;font-weight:600;color:var(--ink)}
.sec-sub{position:absolute;left:0;width:1200px;text-align:center;font-size:12.5px;line-height:20px;color:var(--muted)}

/* welcome */
.welcome h2{position:absolute;left:637px;top:806px;font-size:35px;font-weight:600}
.welcome p{position:absolute;left:637px;width:410px;font-size:12.5px;line-height:19.5px;color:var(--muted)}

/* steps */
.step-num{position:absolute;width:260px;text-align:center;font-size:48px;font-weight:700;color:#f6d3b6;top:1322px}
.step{position:absolute;top:1366px;width:260px;height:341px;background:var(--white);border-radius:14px;box-shadow:0 4px 18px rgba(20,40,70,.12);text-align:center}
.step h3{position:absolute;left:0;top:196px;width:100%;font-size:18.5px;font-weight:600;line-height:25px;color:var(--navy)}
.step p{position:absolute;left:35px;top:258px;width:190px;font-size:12.5px;line-height:20px;color:var(--muted)}
.step .ph{left:30px;top:30px;width:200px;height:150px}
.step-arrow{position:absolute;top:1528px;width:36px;height:26px}

/* services */
.services-title{color:var(--white);top:1775px}
.svc-label{position:absolute;font-size:17px;font-weight:600;line-height:24px;color:var(--white)}
.svc-label.left{text-align:right}
.svc-icon{position:absolute;width:72px;height:72px;border-radius:50%;background:var(--orange);border:4px solid var(--orange-soft);box-shadow:0 0 0 3px rgba(232,128,47,.35)}
.svc-icon::after{content:"";position:absolute;left:18px;top:18px;width:28px;height:28px;border:2.5px solid var(--white);border-radius:6px}
.hub{position:absolute;left:481px;top:1898px;width:238px;height:238px;border-radius:50%;background:var(--white);border:5px solid var(--navy);box-shadow:0 0 0 6px var(--white);display:flex;align-items:center;justify-content:center}
.hub .logo{font-size:34px}

/* resources */
.res{position:absolute;top:2523px;width:330px;text-align:center}
.res .ph{position:relative;margin:0 auto;width:300px;height:207px}
.res h3{margin-top:36px;font-size:16.5px;font-weight:600;line-height:24px}
.res p{margin-top:16px;font-size:12.5px;line-height:19.5px;color:var(--muted)}

/* contact */
.contact h2{position:absolute;left:84px;top:3036px;font-size:35px;font-weight:600}
.contact .sub{position:absolute;left:84px;top:3099px;width:320px;font-size:12.5px;line-height:20px;color:var(--muted)}
.field{position:absolute;height:44px;border:1.5px solid var(--line);border-radius:24px;background:var(--white);display:flex;align-items:center;padding-left:52px;font-size:12.5px;color:var(--ink)}
.field.focus{border-color:var(--navy)}
.field svg{position:absolute;left:20px;top:13px;width:16px;height:16px}
.field .sep{position:absolute;left:42px;top:12px;width:1px;height:20px;background:var(--line)}
.field.msg{height:60px;align-items:flex-start;padding-top:12px;border-radius:30px}

/* newsletter */
.news-title{position:absolute;left:0;width:1200px;top:3655px;text-align:center;font-size:30px;font-weight:600;line-height:38px;color:var(--white)}
.news-sub{position:absolute;left:0;width:1200px;top:3730px;text-align:center;font-size:12.5px;line-height:20px;color:var(--white)}
.news-form{left:366px;top:3784px;width:468px;height:48px;border:1.5px solid var(--white);border-radius:8px}
.news-form .input{position:absolute;left:20px;top:14px;font-size:12.5px;color:var(--white)}
.news-form .send{position:absolute;right:6px;top:5px;width:132px;height:36px;background:var(--white);border-radius:6px;color:var(--orange);font-weight:600;font-size:14px;display:flex;align-items:center;justify-content:center}
.rule{position:absolute;left:60px;width:1080px;height:1px;background:rgba(255,255,255,.45)}
.info{position:absolute;top:3914px;display:flex;align-items:center;gap:14px;font-size:14px;color:var(--white)}
.info .ic{width:38px;height:38px;border-radius:50%;background:var(--navy);border:2px solid var(--white);display:flex;align-items:center;justify-content:center}
.foot-links{position:absolute;top:4002px;font-size:12.5px;color:var(--white);display:flex;gap:20px}
.foot-links i{font-style:normal;opacity:.8}
.copyright{position:absolute;left:0;width:1200px;top:4068px;text-align:center;font-size:12px;color:var(--white)}
</style>
</head>
<body>

<!-- background bands -->
<svg class="bg-shape" viewBox="0 0 1200 4101" aria-hidden="true">
  <path d="M0 0H1200V545C1010 572 700 600 600 716C500 600 190 572 0 545Z" fill="var(--navy)"/>
  <path d="M0 1540H1200V2165C1010 2192 700 2218 600 2332C500 2218 190 2192 0 2165Z" fill="var(--navy)"/>
  <rect x="0" y="3400" width="1200" height="701" fill="var(--orange)"/>
  <path d="M0 2969H1200V3440C1010 3468 700 3490 600 3590C500 3490 190 3468 0 3440Z" fill="var(--light)"/>
</svg>

<!-- navigation -->
<header class="abs nav">
  <div class="logo"><span class="dot"></span>BRIMCORE</div>
  <nav class="nav-links">
    <span class="active" style="left:328px">Home</span>
    <span style="left:418px">About US</span>
    <span style="left:515px">Services</span>
    <span style="left:628px">How It Works</span>
    <span style="left:747px">Resources</span>
    <span style="left:849px">Contact</span>
  </nav>
  <a class="btn" style="left:914px;top:24px;width:150px;height:41px">Get Started</a>
</header>

<!-- hero -->
<h1 class="abs hero-title">THE <em>TRAFFIC</em><br><em>CONTROLLER</em> FOR<br>YOUR DIGITAL ACCESS</h1>
<p class="abs hero-text">BrimCore enforces secure, consistent, and automated access control across your apps, servers, and AI tools.</p>
<a class="btn" style="left:60px;top:452px;width:150px;height:42px">Get Started</a>
<a class="btn ghost" style="left:216px;top:452px;width:160px;height:42px">How It Works</a>
<div class="ph" role="img" aria-label="Isometric illustration of cloud security shield, servers and laptops linked by circuit lines" style="left:668px;top:135px;width:400px;height:454px;background:radial-gradient(circle at 50% 50%,#4f8fd1 0%,#2f5f93 45%,rgba(31,59,97,0) 75%)"></div>

<!-- welcome -->
<section class="welcome">
  <div class="ph" role="img" aria-label="Isometric illustration of a person working beside data server racks, charts and devices" style="left:120px;top:772px;width:453px;height:382px;background:linear-gradient(160deg,#e4f5f9,#cfe4f2 55%,#f7efe6)"></div>
  <h2>WELCOME BRIMCORE</h2>
  <p style="top:866px">Lorem Ipsum has been the industry's standard dummy text ever since the 1500s, when an unknown printer took a galley of type and scrambled it to make a type specimen book. It has survived not only five centuries, but also the leap into electronic typesetting, remaining essentially unchanged.</p>
  <p style="top:971px">Lorem Ipsum has been the industry's standard dummy text ever since the 1500s, when an unknown printer took a galley of type and scrambled it to make a type specimen book. It has survived not only five centuries, but also the leap into electronic typesetting, remaining essentially unchanged.</p>
  <a class="btn" style="left:636px;top:1092px;width:150px;height:39px">View More</a>
</section>

<!-- how it works -->
<h2 class="sec-title" style="top:1222px">HOW IT WORKS</h2>
<p class="sec-sub" style="top:1280px">Lorem Ipsum has been the industry's standard dummy text<br>ever since the 1500s.</p>

<div class="step-num" style="left:154px">01</div>
<div class="step-num" style="left:471px">02</div>
<div class="step-num" style="left:788px">03</div>

<article class="step" style="left:154px">
  <div class="ph" role="img" aria-label="Illustration of fingerprint login on a phone with rating card and envelope" style="background:linear-gradient(160deg,#eaf1fb,#dce8f6 60%,#fbeede)"></div>
  <h3>Precise Access<br>Control</h3>
  <p>Each user, app, or bot gets access only to what's necessary.</p>
</article>
<article class="step" style="left:471px">
  <div class="ph" role="img" aria-label="Illustration of a team reviewing security policies at a desk" style="background:linear-gradient(160deg,#eaf1fb,#d9e6f4 60%,#eef6e6)"></div>
  <h3>Consistent<br>Enforcement</h3>
  <p>Policies apply everywhere — across servers, APIs, and AI integrations.</p>
</article>
<article class="step" style="left:788px">
  <div class="ph" role="img" aria-label="Illustration of people automating policy workflows with laptops" style="background:linear-gradient(160deg,#eaf1fb,#d6e4f4 60%,#e9f4ea)"></div>
  <h3>Policy<br>Automation</h3>
  <p>Build once, enforce automatically at scale.</p>
</article>

<svg class="step-arrow" style="left:424px" viewBox="0 0 36 26" aria-hidden="true"><path d="M2 13H30M20 3L32 13L20 23" fill="none" stroke="var(--orange)" stroke-width="4"/></svg>
<svg class="step-arrow" style="left:741px" viewBox="0 0 36 26" aria-hidden="true"><path d="M2 13H30M20 3L32 13L20 23" fill="none" stroke="var(--orange)" stroke-width="4"/></svg>

<!-- services -->
<h2 class="sec-title services-title">OUR SERVICES</h2>
<svg class="abs" style="left:0;top:0;width:1200px;height:4101px;pointer-events:none" viewBox="0 0 1200 4101" aria-hidden="true">
  <path d="M441 1896C395 1940 395 2094 441 2138" fill="none" stroke="var(--orange)" stroke-width="2"/>
  <path d="M758 1896C805 1940 805 2094 758 2138" fill="none" stroke="var(--orange)" stroke-width="2"/>
</svg>
<div class="svc-icon" style="left:405px;top:1860px"></div>
<div class="svc-icon" style="left:368px;top:1981px"></div>
<div class="svc-icon" style="left:405px;top:2102px"></div>
<div class="svc-icon" style="left:722px;top:1860px"></div>
<div class="svc-icon" style="left:758px;top:1981px"></div>
<div class="svc-icon" style="left:722px;top:2102px"></div>
<div class="hub"><div class="logo">BRIMCORE</div></div>

<div class="svc-label left" style="left:177px;width:200px;top:1871px">Access Control<br>Management</div>
<div class="svc-label left" style="left:140px;width:200px;top:1991px">Identity &amp; Policy<br>Enforcement</div>
<div class="svc-label left" style="left:132px;width:245px;top:2111px">AI &amp; Automation<br>Access Governance</div>
<div class="svc-label" style="left:820px;width:260px;top:1871px">Compliance &amp; Audit<br>Support</div>
<div class="svc-label" style="left:857px;width:260px;top:1991px">Integration &amp;<br>Deployment Services</div>
<div class="svc-label" style="left:820px;width:260px;top:2111px">Monitoring &amp; Continuous<br>Improvement</div>

<!-- resources -->
<h2 class="sec-title" style="top:2400px">RESOURCES</h2>
<p class="sec-sub" style="top:2455px">Lorem Ipsum has been the industry's standard dummy text ever since<br>the 1500s, when an unknown printer took a galley.</p>

<article class="res" style="left:71px">
  <div class="ph" role="img" aria-label="Illustration of a person with fingerprint phone login and rating card" style="background:linear-gradient(160deg,#e8f1fb,#d7e6f5 60%,#f6eee2)"></div>
  <h3>Lorem Ipsum Has Been<br>The Industry's</h3>
  <p>Lorem Ipsum has been the industry's standard dummy text ever since the 1500s, when an unknown printer took a galley of type and scrambled.</p>
</article>
<article class="res" style="left:435px">
  <div class="ph" role="img" aria-label="Illustration of a secured monitor with documents, folder and padlock" style="background:linear-gradient(160deg,#e8f1fb,#d5e3f3 60%,#f6ead9)"></div>
  <h3>Lorem Ipsum Has Been<br>The Industry's</h3>
  <p>Lorem Ipsum has been the industry's standard dummy text ever since the 1500s, when an unknown printer took a galley of type and scrambled.</p>
</article>
<article class="res" style="left:800px">
  <div class="ph" role="img" aria-label="Illustration of an AI assistant on screen with dashboards and people" style="background:linear-gradient(160deg,#e8f1fb,#d6e4f4 60%,#f7eedd)"></div>
  <h3>Lorem Ipsum Has Been<br>The Industry's</h3>
  <p>Lorem Ipsum has been the industry's standard dummy text ever since the 1500s, when an unknown printer took a galley of type and scrambled.</p>
</article>

<!-- contact -->
<section class="contact">
  <h2>CONTACT US</h2>
  <p class="sub">Lorem Ipsum has been the industry's standard dummy text ever since the 1500s.</p>

  <div class="field focus" style="left:84px;top:3156px;width:188px">
    <svg viewBox="0 0 16 16"><circle cx="8" cy="5" r="3.5" fill="var(--navy)"/><path d="M1.5 16C1.5 11 4.5 9.5 8 9.5S14.5 11 14.5 16Z" fill="var(--navy)"/></svg><span class="sep"></span>First Name*</div>
  <div class="field" style="left:280px;top:3156px;width:188px">
    <svg viewBox="0 0 16 16"><circle cx="8" cy="5" r="3.5" fill="var(--navy)"/><path d="M1.5 16C1.5 11 4.5 9.5 8 9.5S14.5 11 14.5 16Z" fill="var(--navy)"/></svg><span class="sep"></span>Last Name*</div>
  <div class="field" style="left:82px;top:3216px;width:188px">
    <svg viewBox="0 0 16 16"><rect x="1" y="3" width="14" height="10" rx="1.5" fill="var(--navy)"/><path d="M1.5 4L8 9L14.5 4" fill="none" stroke="#fff" stroke-width="1.3"/></svg><span class="sep"></span>Email*</div>
  <div class="field" style="left:279px;top:3216px;width:188px">
    <svg viewBox="0 0 16 16"><path d="M3 1L6 1L7 5L5 6.5C6 8.8 7.2 10 9.5 11L11 9L15 10V13C15 14 14 15 13 15C6.5 15 1 9.5 1 3C1 2 2 1 3 1Z" fill="var(--navy)"/></svg><span class="sep"></span>Phone No*</div>
  <div class="field msg" style="left:84px;top:3276px;width:385px">
    <svg viewBox="0 0 16 16" style="top:16px"><path d="M1 2H11V9H5L2 11.5V9H1Z" fill="var(--navy)"/><path d="M12 5H15V12H14V14L11.5 12H6V10H12Z" fill="var(--navy)"/></svg><span class="sep" style="top:14px"></span>Messages*</div>

  <a class="btn" style="left:83px;top:3364px;width:150px;height:39px">View More</a>

  <div class="ph" role="img" aria-label="Illustration of people around a laptop with a padlock folder, gears and security alerts" style="left:581px;top:3017px;width:486px;height:453px;background:radial-gradient(circle at 55% 50%,#f3d49c 0%,#cfdff0 40%,rgba(245,246,248,0) 72%)"></div>
</section>

<!-- newsletter & footer -->
<h2 class="news-title">SUBSCRIBE TO OUR<br>NEWSLETTER</h2>
<p class="news-sub">Lorem Ipsum has been the industry's standard dummy text ever<br>since the 1500s, when an unknown printer took.</p>
<form class="abs news-form">
  <span class="input">Enter Your Email</span>
  <span class="send">SEND NOW</span>
</form>

<div class="rule" style="top:3893px"></div>

<div class="info" style="left:264px">
  <span class="ic"><svg width="16" height="16" viewBox="0 0 16 16"><path d="M3 1L6 1L7 5L5 6.5C6 8.8 7.2 10 9.5 11L11 9L15 10V13C15 14 14 15 13 15C6.5 15 1 9.5 1 3C1 2 2 1 3 1Z" fill="#fff"/></svg></span>+ 0123 456 789
</div>
<div class="info" style="left:514px">
  <span class="ic"><svg width="16" height="16" viewBox="0 0 16 16"><rect x="1" y="3" width="14" height="10" rx="1.5" fill="#fff"/><path d="M1.5 4L8 9L14.5 4" fill="none" stroke="var(--navy)" stroke-width="1.3"/></svg></span>info@brimcore.example
</div>
<div class="info" style="left:769px">
  <span class="ic"><svg width="16" height="16" viewBox="0 0 16 16"><path d="M8 1C5 1 3 3.2 3 6C3 9.5 8 15 8 15S13 9.5 13 6C13 3.2 11 1 8 1Z" fill="#fff"/><circle cx="8" cy="6" r="2" fill="var(--navy)"/></svg></span>brimcore company...
</div>

<div class="foot-links" style="left:236px"><span>Home</span><i>|</i><span>About Us</span><i>|</i><span>Services</span></div>
<div class="logo abs" style="left:550px;top:4000px;font-size:18px;color:var(--white)">BRIMCORE</div>
<div class="foot-links" style="left:746px"><span>How it Work</span><i>|</i><span>Resources</span><i>|</i><span>Contact Us</span></div>

<div class="rule" style="top:4046px"></div>
<p class="copyright">© Copyright 2025 brimcore.All Rights Reserved</p>

</body>
</html>
```